Business Card Design for Orthopaedic Surgeon

This is a double-sided glossy business card. I prefer baby blue, teal, and green as color schemes. I have my logo already (many colors that you can choose from). I have photos and examples of my old card (very bland but has the information in it). I also have one that my assistant tried to design, but the writing is too small and I don't love the formatting. But it is close!
I would like my logo to be on the business card but I'm uploading my logo in many different colors so you can choose which one looks best based on the color scheme. I also uploaded many sized headshots so you can choose the best resolution one.

Additional information:
Correct business address:
4382 NW 58th Lane, Suite 305
Brookfield, OH 33417

Everything else on both business cards are accurate.

I actually need 2 different business cards generated. One that includes my cell phone number-- Personal cell: 585-314-9062 in addition to Office phone: (954) 316-4870 and Office Fax: 954-316-4881. Again, one card would have my personal cell and one wouldn't

Overall I just think the baby blue card (uploaded) is missing something on the front--of course it is also missing my office phone/fax/personal cell. I do want my website on the front too. Email: info@wellsorthocare.example

You can use your discretion about what goes on the front vs. what goes on the back to eliminated clutter.

Oh and on the back, I would like to list "Conditions Treated" (not specialties include). The list is:
Carpal Tunnel
Trigger Finger
Ganglion Cysts
Hand Tumors
Han & Wrist Arthritis
Hand, Wrist & Elbow Tendonitis
Fractures of the Hand, Wrist, Elbow and Humerus
Nerve Injuries of the Hand, Wrist & Elbow
Microsurgery
Wrist Arthroscopy
Endoscopic Surgery

Target Market(s)

Primary care doctors, Lawyers, patients

Industry/Entity Type

Medical

Contact Information for Business Card

Please see above in project description

Colors

Designer to choose colors to be used in the design.

Requirements
Must have
• -Correct office info, Board Certified Orthopaedic Hand & Upper Extremity Surgeon
Nice to have
• Something that is classy and wow!

```html
<!DOCTYPE html>
<html lang="en">
<head>
<meta charset="utf-8">
<title>Dana Wells M.D. — Business Card</title>
<link href="https://fonts.googleapis.com/css2?family=Montserrat:wght@300;400;500;600;700&display=swap" rel="stylesheet">
<style>
  :root {
    --backdrop: #2c2f33;
    --navy: #04263b;
    --navy-deep: #021a2a;
    --sky: #1e9ad6;
    --ink: #101418;
    --grey: #6a6d70;
    --white: #ffffff;
    --photo-a: #d9d6d2;
    --photo-b: #2a2522;
  }
  * { box-sizing: border-box; margin: 0; padding: 0; }
  html, body { width: 1200px; height: 1097px; overflow: hidden; }
  body {
    background: var(--backdrop);
    font-family: "Montserrat", sans-serif;
    position: relative;
  }
  .card {
    position: absolute;
    top: 402px;
    width: 512px;
    height: 292px;
    overflow: hidden;
  }
  /* Front */
  .card-front { left: 70px; background: var(--white); }
  .front-edge {
    position: absolute; right: 0; top: 0; width: 29px; height: 100%;
    background: var(--navy);
  }
  .front-photo {
    position: absolute; left: 315px; top: 0; width: 168px; height: 100%;
    background: linear-gradient(180deg, var(--photo-a) 0%, #8a7468 45%, var(--photo-b) 100%);
  }
  .doctor-name {
    position: absolute; left: 17px; top: 37px;
    font-size: 30px; font-weight: 700; letter-spacing: -0.5px;
    color: var(--ink); white-space: nowrap;
  }
  .doctor-name .first { color: var(--sky); }
  .doctor-title {
    position: absolute; left: 17px; top: 77px; width: 290px;
    text-align: center; font-size: 15.5px; font-weight: 300;
    color: var(--grey); line-height: 20px; letter-spacing: 0.6px;
  }
  .contact-panel {
    position: absolute; left: 0; top: 125px; width: 253px; height: 101px;
    background: var(--navy); padding: 6px 0 0 22px;
    list-style: none;
  }
  .contact-panel li {
    display: flex; align-items: center; height: 24.5px;
    color: var(--white); font-size: 14.5px; font-weight: 600; white-space: nowrap;
  }
  .contact-panel svg { width: 13px; height: 13px; margin-right: 12px; fill: var(--white); flex: none; }
  .contact-panel li.small { font-size: 12px; }
  .address {
    position: absolute; left: 34px; top: 236px;
    font-size: 15.5px; font-weight: 400; color: var(--ink); line-height: 19px;
  }
  /* Back */
  .card-back {
    left: 618px;
    background: radial-gradient(ellipse 55% 75% at 45% 55%, var(--sky) 0%, #0d5f8c 40%, var(--navy) 75%, var(--navy-deep) 100%);
    color: var(--white);
  }
  .conditions-heading {
    position: absolute; left: 34px; top: 22px;
    font-size: 17px; font-weight: 600; letter-spacing: 0.2px;
  }
  .conditions-list {
    position: absolute; left: 78px; top: 51px;
    list-style: none;
  }
  .conditions-list li {
    position: relative; font-size: 15px; font-weight: 500; line-height: 20.3px; white-space: nowrap;
  }
  .conditions-list li::before {
    content: ""; position: absolute; left: -20px; top: 8px;
    width: 5px; height: 5px; border-radius: 50%; background: var(--white);
  }
  .brand {
    position: absolute; left: 355px; top: 34px; width: 118px; height: 118px;
    border: 2.5px solid var(--white); border-radius: 50%;
    display: flex; align-items: center; justify-content: center; text-align: center;
    font-size: 16px; font-weight: 700; line-height: 20px; letter-spacing: 1px; color: var(--white);
  }
</style>
</head>
<body>
  <section class="card card-front" aria-label="Business card front">
    <h1 class="doctor-name"><span class="first">DANA</span> WELLS M.D.</h1>
    <p class="doctor-title">board certified orthopedic<br>hand &amp; upper extremity surgeon</p>
    <ul class="contact-panel">
      <li><svg viewBox="0 0 24 24"><path d="M6.6 10.8a15 15 0 0 0 6.6 6.6l2.2-2.2c.3-.3.7-.4 1-.2 1.1.4 2.3.6 3.6.6.6 0 1 .4 1 1V20c0 .6-.4 1-1 1A17 17 0 0 1 3 4c0-.6.4-1 1-1h3.5c.6 0 1 .4 1 1 0 1.3.2 2.5.6 3.6.1.3 0 .7-.2 1z"/></svg>(555) 316-4870</li>
      <li><svg viewBox="0 0 24 24"><path d="M6 2h12v6H6zM3 9h18a1 1 0 0 1 1 1v8h-4v4H6v-4H2v-8a1 1 0 0 1 1-1zm5 8v3h8v-3z"/></svg>(555) 316-4881</li>
      <li class="small"><svg viewBox="0 0 24 24"><path d="M2 5h20v2l-10 6L2 7zm0 4.3 10 6 10-6V19H2z"/></svg>info@wellsorthocare.example</li>
      <li class="small"><svg viewBox="0 0 24 24"><path d="M12 2a10 10 0 1 0 0 20 10 10 0 0 0 0-20zm6.9 6h-3a15 15 0 0 0-1.3-3.9A8 8 0 0 1 18.9 8zM12 4c.8 1.2 1.5 2.5 1.9 4h-3.8c.4-1.5 1.1-2.8 1.9-4zM4.3 14a8 8 0 0 1 0-4h3.4a16 16 0 0 0 0 4zm.8 2h3a15 15 0 0 0 1.3 3.9A8 8 0 0 1 5.1 16zm3-8h-3a8 8 0 0 1 4.3-3.9C8.8 5.3 8.4 6.6 8.1 8zM12 20c-.8-1.2-1.5-2.5-1.9-4h3.8c-.4 1.5-1.1 2.8-1.9 4zm2.3-6H9.7a14 14 0 0 1 0-4h4.6a14 14 0 0 1 0 4zm.3 5.9c.6-1.2 1-2.5 1.3-3.9h3a8 8 0 0 1-4.3 3.9zm1.7-5.9a16 16 0 0 0 0-4h3.4a8 8 0 0 1 0 4z"/></svg>www.wellsorthocare.example</li>
    </ul>
    <p class="address">4382 NW 58th Lane, Suite 305<br>Brookfield, OH 33417</p>
    <div class="front-photo" role="img" aria-label="Headshot of the surgeon in a dark blazer"></div>
    <div class="front-edge"></div>
  </section>

  <section class="card card-back" aria-label="Business card back">
    <h2 class="conditions-heading">CONDITIONS TREATED</h2>
    <ul class="conditions-list">
      <li>Carpal Tunnel</li>
      <li>Trigger Finger</li>
      <li>Ganglion Cysts</li>
      <li>Hand Tumors</li>
      <li>Hand &amp; Wrist Arthritis</li>
      <li>Hand, Wrist &amp; Elbow Tendonitis</li>
      <li>Fractures of the Hand, Wrist, Elbow &amp; Humerus</li>
      <li>Nerve Injuries of the Hand, Wrist &amp; Elbow</li>
      <li>Microsurgery</li>
      <li>Wrist Arthroscopy</li>
      <li>Endoscopic Surgery</li>
    </ul>
    <div class="brand">WELLS<br>HAND</div>
  </section>
</body>
</html>
```